Business Card Design

Please use the Logo for colors and styles, and create a business card using the following info:

Matthias Loeber
Web Developer

Loeber Solutions
+41 76 482 17 05
matthias@loeber-solutions.example
www.loeber-solutions.example

Download the logo at http://loeber-solutions.example/tl_files/loeber_solutions.zip

Thanks for your works!

```html
<!DOCTYPE html>
<html lang="en">
<head>
<meta charset="UTF-8">
<title>Loeber Solutions – Business Card</title>
<link rel="stylesheet" href="https://fonts.googleapis.com/css2?family=Questrial&display=swap">
<style>
  :root {
    --backdrop: #6f6f6f;
    --card-black: #1c1c1c;
    --band-grey: #7b7b7b;
    --box-grey: #5f5f5f;
    --ink-white: #ffffff;
  }
  * { margin: 0; padding: 0; box-sizing: border-box; }
  html, body {
    width: 1200px;
    height: 900px;
    overflow: hidden;
    background: var(--backdrop);
    font-family: "Questrial", sans-serif;
  }
  .stage {
    position: relative;
    width: 1200px;
    height: 900px;
  }
  .business-card {
    position: absolute;
    left: 160px;
    top: 200px;
    width: 880px;
    height: 500px;
    background: var(--card-black);
    overflow: hidden;
    box-shadow: 0 10px 30px rgba(0,0,0,0.35);
  }
  .card-band {
    position: absolute;
    inset: 0;
    width: 880px;
    height: 500px;
  }
  .card-band path { fill: var(--band-grey); }
  .brand-name {
    position: absolute;
    left: 62px;
    top: 62px;
    color: var(--ink-white);
    font-size: 64px;
    letter-spacing: 2px;
    line-height: 1;
    text-transform: uppercase;
    white-space: nowrap;
  }
  .name-box {
    position: absolute;
    left: 40px;
    top: 212px;
    width: 420px;
    height: 104px;
    background: var(--box-grey);
    color: var(--ink-white);
    text-transform: uppercase;
    font-size: 34px;
    letter-spacing: 2px;
    line-height: 42px;
    padding: 11px 0 0 70px;
    white-space: nowrap;
  }
  .address-box {
    position: absolute;
    left: 520px;
    top: 192px;
    width: 300px;
    height: 88px;
    background: var(--box-grey);
    color: var(--ink-white);
    font-style: normal;
    text-transform: uppercase;
    font-size: 15px;
    letter-spacing: 1px;
    line-height: 21px;
    padding: 13px 0 0 20px;
    white-space: nowrap;
  }
  .contact-box {
    position: absolute;
    left: 0;
    top: 330px;
    width: 640px;
    height: 104px;
    background: var(--box-grey);
    color: var(--ink-white);
    text-transform: uppercase;
    font-size: 19px;
    letter-spacing: 1px;
    line-height: 26px;
    padding: 13px 0 0 150px;
    white-space: nowrap;
  }
</style>
</head>
<body>
  <main class="stage">
    <section class="business-card" aria-label="Loeber Solutions business card">
      <svg class="card-band" viewBox="0 0 880 500" aria-hidden="true">
        <path d="M0 190 C 300 178, 600 168, 880 160 L 880 330 C 600 342, 300 360, 0 372 Z"/>
        <path d="M0 372 C 300 360, 600 342, 880 330 L 880 352 C 600 370, 300 420, 0 452 Z" opacity="0.55"/>
      </svg>

      <div class="brand-name">Loeber Solutions</div>

      <div class="name-box">
        <p class="person-name">Matthias Loeber</p>
        <p class="person-title">Web Developer</p>
      </div>

      <address class="address-box">
        <p>Loeber Solutions</p>
        <p>Lindenhofweg 12</p>
        <p>CH-8600 Talbrunn</p>
      </address>

      <div class="contact-box">
        <p class="contact-phone">+41 76 482 17 05</p>
        <p class="contact-email">matthias@loeber-solutions.example</p>
        <p class="contact-web">www.loeber-solutions.example</p>
      </div>
    </section>
  </main>
</body>
</html>
```